New College Graduate Resume - Creative and unique design that stands out from the rest

Need creative resume design for recent college graduate who graduated from School of Music with a concentration in music composition and production. Striving for a contemporary layout/design that allows the resume to "be unique" and "stand out" but be polished and professional. Open to integrating moderate color/graphics as part of resume design but the design can be minus those attributes as well. Attached is raw content in 7 sections (name/contact info, education, highlights of qualifications, work experience, honors/awards, and professional affiliations). While the designer has full latitude over overall design which (section headers, font type, separation/spacing, use of bullets, justification of text, etc.) please maintain current order/sequence of the 7 sections.

Industry/Entity Type

School

Requirements
Must have
• Name (Tobias Hale Whitcombe II) should be most prominent (bold/font size) compared to remainder of resume copy.
• Section headers should be prominent but less so when compared to name on resume.
• The attached file of resume content is provided as raw source copy and is NOT to be just copied and pasted into open fields as is. Expectation is each section of copy will be organized in a manner that is most visually appealing and may include bullets, appropriate spacing, etc.
Should not have
• The attached file of resume content is provided as source copy and is NOT to be just copied and pasted into open fields as is. Expectation is each section of copy will be organized in a manner that

```html
<!DOCTYPE html>
<html lang="en">
<head>
<meta charset="utf-8">
<title>Tobias Hale Whitcombe II – Resume</title>
<link rel="stylesheet" href="https://fonts.googleapis.com/css2?family=Open+Sans:wght@400;600&family=Arimo:wght@400&display=swap">
<style>
:root{
  --teal:#9ad3d6;
  --charcoal:#4e4a4b;
  --ink:#4a4a4a;
  --white:#ffffff;
  --label-grey:#ebebeb;
}
*{margin:0;padding:0;box-sizing:border-box}
html,body{width:863px;height:1200px;overflow:hidden;background:var(--white)}
.resume{position:relative;width:863px;height:1200px;overflow:hidden;font-family:"Arimo",Arial,sans-serif;color:var(--ink)}
.abs{position:absolute}
.header{left:0;top:0;width:863px;height:254px;background:var(--teal)}
.badge{left:27px;top:23px;width:150px;height:150px;border-radius:50%;background:var(--white);box-shadow:4px 6px 10px rgba(0,0,0,.18)}
.name{left:236px;top:24px;font-family:"Open Sans",sans-serif;font-weight:400;font-size:35px;color:#444;letter-spacing:-.5px;white-space:nowrap}
.title{left:236px;top:67px;font-family:"Open Sans",sans-serif;font-size:18px;color:#444}
.rule{left:236px;top:97px;width:585px;height:3px;background:var(--white)}
.about-heading{left:236px;top:103px;font-family:"Open Sans",sans-serif;font-weight:400;font-size:21px;color:#444}
.about{left:234px;top:136px;width:575px;font-size:13.6px;line-height:17.2px;color:#444}
.about p+p{margin-top:6px}
.sidebar{left:0;top:269px;width:308px;height:824px;background:var(--charcoal)}
.spine{left:308px;top:269px;width:97px;height:931px;background:var(--teal)}
.side-label{left:0;width:308px;height:32px;background:var(--white);font-family:"Open Sans",sans-serif;font-size:16px;color:#444;line-height:32px;padding-left:78px}
.side-icon{width:56px;height:56px;border-radius:50%;background:var(--teal);display:flex;align-items:center;justify-content:center}
.side-list{left:18px;color:var(--white);list-style:none}
.qualifications li{font-family:"Open Sans",sans-serif;font-size:12.2px;line-height:22px;text-transform:uppercase}
.qualifications li.two{line-height:16px;margin:3px 0 5px}
.plain li{font-size:12.4px;line-height:15.4px;margin-bottom:9px}
.contact{left:18px;font-size:13px;color:#333;display:flex;align-items:center;gap:10px}
.date{width:97px;left:308px;text-align:center;font-family:"Open Sans",sans-serif;font-size:16px;color:#555;line-height:21px}
.section-bar{left:406px;height:32px;background:var(--label-grey);font-family:"Open Sans",sans-serif;font-size:16px;color:#444;line-height:32px;display:flex;align-items:center}
.section-bar .dot{width:30px;height:30px;border-radius:50%;background:var(--teal);margin:0 14px 0 20px;display:flex;align-items:center;justify-content:center}
.job{left:415px}
.job h3{font-family:"Open Sans",sans-serif;font-weight:400;font-size:16.5px;line-height:20px;color:#444}
.job .where{font-family:"Open Sans",sans-serif;font-size:16.5px;line-height:20px;color:#444;padding-left:6px}
.job .role{font-size:12.4px;line-height:15.4px;margin-top:4px;padding-left:6px;color:#333}
.job .duties{font-size:12.4px;line-height:15.4px;padding-left:6px;color:#333}
.school{left:420px;font-family:"Open Sans",sans-serif;font-size:16.5px;line-height:21.5px;color:#444}
</style>
</head>
<body>
<div class="resume">
  <div class="abs header"></div>
  <div class="abs badge" role="img" aria-label="Round personal monogram badge"></div>
  <h1 class="abs name">TOBIAS HALE WHITCOMBE II</h1>
  <div class="abs title">COLLEGE GRADUATE</div>
  <div class="abs rule"></div>
  <h2 class="abs about-heading">About Me</h2>
  <div class="abs about">
    <p>Recent graduate of a highly ranked university seeking opportunities to apply composition and production talents across a variety of music genres and other media. Expertise lies in delivering high quality sound design, editing, mixing, and recording.</p>
    <p>Excellent interpersonal skills and the ability to build strong relationships with people at all levels.&nbsp; Exceptionally motivated self-starter and creative problem solver who enjoys working collaboratively on teams.</p>
  </div>

  <div class="abs sidebar"></div>
  <div class="abs spine"></div>

  <div class="abs side-label" style="top:291px">QUALIFICATIONS</div>
  <div class="abs side-icon" style="left:13px;top:279px">
    <svg width="32" height="26" viewBox="0 0 32 26"><g fill="#4e4a4b"><circle cx="11" cy="15" r="7"/><circle cx="23" cy="7" r="5"/></g><g stroke="#4e4a4b" stroke-width="3"><path d="M11 5v20M1 15h20M4 8l14 14M18 8L4 22"/><path d="M23 0v14M16 7h14M18 2l10 10M28 2L18 12"/></g><circle cx="11" cy="15" r="2.5" fill="#9ad3d6"/><circle cx="23" cy="7" r="2" fill="#9ad3d6"/></svg>
  </div>
  <ul class="abs side-list qualifications" style="top:347px">
    <li class="two">Media production software<br>(SoundDesk 11)</li>
    <li>Sound design</li>
    <li>Sound acoustics</li>
    <li>Studio recording</li>
    <li>Audio editing</li>
    <li>Audio mixing</li>
    <li>Analog/digital board operation</li>
    <li>Music arranging</li>
    <li>Music composition</li>
    <li>Music production</li>
    <li>Composing sheet music</li>
    <li>Singer-songwriter</li>
    <li>Rhythm guitarist</li>
  </ul>

  <div class="abs side-label" style="top:676px">HONORS/AWARDS</div>
  <div class="abs side-icon" style="left:13px;top:664px">
    <svg width="28" height="30" viewBox="0 0 28 30" fill="#4e4a4b"><path d="M7 1h14v9a7 7 0 0 1-14 0z"/><path d="M7 4H2v3a6 6 0 0 0 6 6M21 4h5v3a6 6 0 0 1-6 6" fill="none" stroke="#4e4a4b" stroke-width="2"/><rect x="12" y="16" width="4" height="7"/><rect x="8" y="23" width="12" height="3"/><rect x="6" y="26" width="16" height="3"/></svg>
  </div>
  <ul class="abs side-list plain" style="top:736px;left:16px">
    <li>Best Film and Score: Frights and Frames<br>2015 Competition (Bayview University)</li>
    <li>Eleanor J Whitfield Scholar</li>
    <li>Best New Member,<br>Delta Kappa Omega Fraternity, Inc.</li>
    <li>Bayview University Homecoming King,<br>2012</li>
  </ul>

  <div class="abs side-label" style="top:904px">PROFESSIONAL AFFILIATIONS</div>
  <div class="abs side-icon" style="left:13px;top:892px">
    <svg width="36" height="28" viewBox="0 0 36 28" fill="#4e4a4b"><circle cx="18" cy="5" r="4"/><path d="M12 16a6 6 0 0 1 12 0z"/><circle cx="7" cy="17" r="4"/><path d="M1 28a6 6 0 0 1 12 0z"/><circle cx="29" cy="17" r="4"/><path d="M23 28a6 6 0 0 1 12 0z"/><path d="M18 16v4M10 20h16" stroke="#4e4a4b" stroke-width="1.5" fill="none"/></svg>
  </div>
  <ul class="abs side-list plain" style="top:961px;left:13px">
    <li>Member, Guild of New Music Composers (GNMC)</li>
    <li>Member, American Guild of Songwriters,<br>Composers and Publishers (AGSCP)</li>
    <li>Member, Sound Technology Association (STA)</li>
    <li>Member, Delta Kappa Omega Fraternity,<br>Incorporated</li>
  </ul>

  <div class="abs contact" style="top:1106px">
    <svg width="14" height="20" viewBox="0 0 14 20"><rect x="1" y="1" width="12" height="18" rx="2" fill="none" stroke="#9ad3d6" stroke-width="2"/><rect x="5" y="15" width="4" height="1.6" fill="#9ad3d6"/></svg>404-555-0186
  </div>
  <div class="abs contact" style="top:1140px">
    <svg width="20" height="13" viewBox="0 0 20 13"><rect width="20" height="13" fill="#9ad3d6"/><path d="M0 0l10 7 10-7" fill="none" stroke="#fff" stroke-width="1.5"/></svg>thwhitcombe@mailbox.net
  </div>
  <div class="abs contact" style="top:1170px">
    <svg width="16" height="22" viewBox="0 0 16 22"><path d="M8 0a8 8 0 0 1 8 8c0 6-8 14-8 14S0 14 0 8a8 8 0 0 1 8-8z" fill="#9ad3d6"/><circle cx="8" cy="8" r="3" fill="#fff"/></svg>218 Larkspur Lane - Atlanta, Georgia&nbsp; 30311
  </div>

  <div class="abs section-bar" style="top:269px;width:292px">
    <span class="dot"><svg width="16" height="13" viewBox="0 0 16 13" fill="#4e4a4b"><rect x="0" y="3" width="16" height="10" rx="1.5"/><path d="M5 3V1h6v2" fill="none" stroke="#4e4a4b" stroke-width="1.6"/></svg></span>PROFESSIONAL EXPREIENCE
  </div>

  <div class="abs date" style="top:318px">05. 2014<br>–<br>Present</div>
  <div class="abs job" style="top:318px;width:420px">
    <h3>"Coastline Picture Works (CPW)"</h3>
    <div class="where">Miami, FL</div>
    <div class="role">Sound Engineer</div>
    <div class="duties">Edited and mixed recorded field audio to professional standards.<br>Matched audio with motion picture video to create a seamless product.<br>Recorded automated dialogue replacement (ADR) audio and integrated into motion picture video project using SoundDesk 11.<br>Recorded foley sound effects to be added to film, video, and other media in post-production.<br>Composed and recorded original music to accompany various video projects.</div>
  </div>

  <div class="abs date" style="top:516px">05. 2013<br>--<br>10. 2013</div>
  <div class="abs job" style="top:516px;left:411px;width:250px">
    <h3>"Brightway Retail Group"</h3>
    <div class="where">Atlanta, GA</div>
    <div class="role">Sales Associate</div>
    <div class="duties">Provided customer service, maintained a clean and organized work environment, assisted in sales, and performed cashier responsibilities.</div>
  </div>

  <div class="abs date" style="top:651px">06. 2012<br>–<br>08. 2012</div>
  <div class="abs job" style="top:651px;left:411px;width:300px">
    <h3>"Peach State Civic Action"</h3>
    <div class="where">(Community Outreach Network)</div>
    <div class="where">Atlanta, GA</div>
    <div class="role">On-Site Promoter/Intern</div>
    <div class="duties">Promoted and advertised various campaigns and managed various office tasks, such as setting up site maps and organizing and sorting non-profit donations.</div>
  </div>

  <div class="abs date" style="top:804px">06. 2011<br>–<br>08. 2011</div>
  <div class="abs job" style="top:804px;width:300px">
    <h3>"Meridian Direct Sales, Incorporated"</h3>
    <div class="where">Atlanta, GA</div>
    <div class="role">Product Marketing Consultant</div>
    <div class="duties">Conducted direct sales and marketing of subsidiary product line through establishing a compelling value proposition, overcoming objections, and closing the sale.</div>
  </div>

  <div class="abs" style="left:308px;top:949px;width:98px;height:32px;background:var(--white)"></div>
  <div class="abs section-bar" style="top:949px;width:173px">
    <span class="dot"><svg width="18" height="13" viewBox="0 0 18 13" fill="#4e4a4b"><path d="M9 0l9 4-9 4-9-4z"/><path d="M4 6v4c0 2 10 2 10 0V6L9 8z"/><path d="M16.5 5v5" stroke="#4e4a4b" stroke-width="1"/></svg></span>EDUCATION
  </div>
  <div class="abs school" style="top:992px;left:415px">"Bayview University – Harlow School of Music"<br><span style="padding-left:6px">Coral Springs, Florida</span></div>
  <div class="abs date" style="top:1040px">05. 2016</div>
  <div class="abs school" style="top:1040px">Bachelor of Music<br>Major: Media Writing and Production,<br>GPA 3.20/4.0</div>
  <div class="abs date" style="top:1110px">05. 2011</div>
  <div class="abs school" style="top:1110px">Linwood Preparatory Academy<br>College Park, Georgia<br>High School Diploma with Honors</div>
</div>
</body>
</html>
```